Poster: Meditation course

We would like a simple poster to advertise a 10-day meditation course. We would like something very simple and minimal, nothing fancy. We will be putting this poster up around our local area and leaving it on cafe tables etc. We will also be sending it around digitally.
The poster should include the words below. (Please note that we may want to change these words further along in the process.) And in terms of imagery, something like a lotus flower could work well. (Please see the attached lotus flower and lily image in our newsletters, although it doesn't need to be that old school.) The size can be US Letter size / Europe A4. Please include the attached QR code, and please note that for the digital version we would like hyperlinks for the webpage and email. Many thanks!
Text for the poster:
Meditation produces a calm mind
10-day residential meditation course
Half Moon Bay, California
7-17th June 2024
Vipassana meditation in the Theravada Buddhism tradition as taught by Tharamin U Lo Pwint and Mother Dawkelanyi
To apply: https://www.quietriverretreathouse.org/
For more information contact: info@quietriverretreathouse.org
Target Market(s)
Primarily university students. Also other people in California
Look and feel
Each slider illustrates characteristics of the customer's brand and the style your logo design should communicate.

```html
<!DOCTYPE html>
<html lang="en">
<head>
<meta charset="utf-8">
<title>10-Day Residential Meditation Course</title>
<link rel="stylesheet" href="https://fonts.googleapis.com/css2?family=Montserrat:wght@300;400;700;800&display=swap">
<style>
  :root {
    --stage: #808080;
    --paper: #ffffff;
    --ink: #2b2a2b;
    --mist: #e9e8e9;
    --lavender: #cfaad1;
    --lotus-light: #fbeef2;
    --lotus-pink: #e8a6c3;
    --lotus-deep: #c9648f;
    --frame-line: #555555;
  }
  * { margin: 0; padding: 0; box-sizing: border-box; }
  html, body {
    width: 1200px; height: 1200px; overflow: hidden;
    background: var(--stage);
    font-family: "Montserrat", sans-serif;
    color: var(--ink);
  }
  .poster {
    position: absolute; left: 241px; top: 135px;
    width: 718px; height: 929px;
    background: var(--paper);
    overflow: hidden;
  }
  .poster__body {
    position: absolute; left: 0; top: 0; width: 100%; height: 847px;
    background: linear-gradient(180deg,
      var(--paper) 0px, var(--paper) 225px,
      var(--mist) 430px, #dcd6dc 560px,
      #d4c0d5 700px, var(--lavender) 847px);
  }
  .poster__lotus {
    position: absolute; left: 0; top: 440px; width: 718px; height: 407px;
  }
  .tagline {
    position: absolute; top: 48px; width: 100%; text-align: center;
    font-weight: 300; font-size: 20.5px; letter-spacing: 0.3px;
  }
  .title {
    position: absolute; top: 118px; width: 100%; text-align: center;
    font-weight: 800; font-size: 45px; line-height: 52px;
    letter-spacing: 0.2px; text-transform: uppercase;
  }
  .venue {
    position: absolute; left: 169px; top: 307px; width: 379px; height: 67px;
    border: 1px solid var(--frame-line);
    display: flex; flex-direction: column; justify-content: center;
    text-align: center; font-weight: 700; font-size: 20.5px; line-height: 29px;
  }
  .lineage {
    position: absolute; top: 414px; width: 100%; text-align: center;
    font-weight: 400; font-size: 17.5px; line-height: 26px;
  }
  .apply {
    position: absolute; top: 780px; width: 100%; text-align: center;
    font-size: 15.5px; line-height: 23px;
  }
  .contact {
    position: absolute; top: 866px; width: 100%; text-align: center;
    font-size: 15.5px; line-height: 23px;
  }
  .apply a, .contact a { color: var(--ink); text-decoration: none; font-weight: 700; }
  .apply a { font-size: 15.5px; }
  .contact a { font-size: 16px; }
</style>
</head>
<body>
  <main class="poster">
    <div class="poster__body">
      <svg class="poster__lotus" role="img" aria-label="Photo of a hand silhouette holding a glowing pink lotus flower" viewBox="0 0 718 407">
        <defs>
          <radialGradient id="lotusGlow" cx="0.5" cy="0.5" r="0.5">
            <stop offset="0" stop-color="var(--lotus-light)"/>
            <stop offset="0.3" stop-color="var(--lotus-pink)" stop-opacity="0.9"/>
            <stop offset="0.65" stop-color="var(--lotus-deep)" stop-opacity="0.45"/>
            <stop offset="1" stop-color="var(--lotus-deep)" stop-opacity="0"/>
          </radialGradient>
          <radialGradient id="handShade" cx="0.5" cy="0.5" r="0.5">
            <stop offset="0" stop-color="#3a2a34" stop-opacity="0.35"/>
            <stop offset="1" stop-color="#3a2a34" stop-opacity="0"/>
          </radialGradient>
        </defs>
        <ellipse cx="120" cy="340" rx="150" ry="90" fill="url(#handShade)"/>
        <ellipse cx="275" cy="170" rx="210" ry="140" fill="url(#lotusGlow)"/>
      </svg>
    </div>

    <p class="tagline">MEDITATION PRODUCES A CALM MIND</p>

    <h1 class="title">10-Day<br>Residential<br>Meditation Course</h1>

    <div class="venue">
      <span>HALF MOON BAY, CALIFORNIA</span>
      <span>7-17TH JUNE 2024</span>
    </div>

    <p class="lineage">Vipassana meditation in the Theravada<br>Buddhism tradition as taught by Tharamin<br>U Lo Pwint and Mother Dawkelanyi</p>

    <p class="apply">To apply:<br><a href="https://www.quietriverretreathouse.org/">https://www.quietriverretreathouse.org/</a></p>

    <p class="contact">For more information&nbsp; contact:<br><a href="mailto:info@quietriverretreathouse.org">info@quietriverretreathouse.org</a></p>
  </main>
</body>
</html>
```